political election

Elect Ramiro Duval

for

Pellwick School Board Pl. ?

colors used are red, white, and blue

any other graphics are more than welcome.

need this in fine print at bottom

advertising paid for by candidate

Target Market(s)

voters of the school district

Industry/Entity Type

School

Requirements
Must have
• red white and blue and in fine print advertisement paid for by candidate.
Nice to have
• graphics, art

```html
<!DOCTYPE html>
<html lang="en">
<head>
<meta charset="utf-8">
<title>Vote for Ramiro Duval</title>
<link rel="stylesheet" href="https://fonts.googleapis.com/css2?family=Bebas+Neue&display=swap">
<style>
  :root {
    --wood-top: #c9351a;
    --wood-mid: #e4521f;
    --wood-floor: #f06a24;
    --seal-red: #e1231f;
    --seal-blue-light: #4cbce9;
    --seal-blue-dark: #23409a;
    --ink-white: #ffffff;
  }
  html, body {
    margin: 0;
    padding: 0;
    overflow: hidden;
    background: #ffffff;
  }
  .poster {
    position: relative;
    width: 850px;
    height: 1200px;
    overflow: hidden;
  }
  .poster__backdrop {
    position: absolute;
    inset: 0;
    background:
      radial-gradient(ellipse 70% 45% at 50% 78%, rgba(255,150,60,0.45), transparent 70%),
      linear-gradient(180deg, var(--wood-top) 0%, var(--wood-mid) 50%, var(--wood-floor) 80%, var(--wood-mid) 100%);
  }
  .poster__art {
    position: absolute;
    inset: 0;
    width: 850px;
    height: 1200px;
  }
  .headline, .candidate-name, .office, .office-seat, .event-info, .fine-print {
    font-family: "Bebas Neue", "Arial Narrow", sans-serif;
    fill: var(--ink-white);
  }
  .fine-print {
    font-size: 20px;
    letter-spacing: 1.5px;
  }
</style>
</head>
<body>
<main class="poster">
  <div class="poster__backdrop" role="img" aria-label="Warm orange-red wooden plank wall curving into a wooden floor"></div>

  <svg class="poster__art" viewBox="0 0 850 1200" xmlns="http://www.w3.org/2000/svg">
    <defs>
      <path id="seal-shape" d="M96.58,-17.22 Q110,0 96.58,17.22 Q83.15,34.44 80.47,56.11 Q77.78,77.78 56.11,80.47 Q34.44,83.15 17.22,96.58 Q0,110 -17.22,96.58 Q-34.44,83.15 -56.11,80.47 Q-77.78,77.78 -80.47,56.11 Q-83.15,34.44 -96.58,17.22 Q-110,0 -96.58,-17.22 Q-83.15,-34.44 -80.47,-56.11 Q-77.78,-77.78 -56.11,-80.47 Q-34.44,-83.15 -17.22,-96.58 Q0,-110 17.22,-96.58 Q34.44,-83.15 56.11,-80.47 Q77.78,-77.78 80.47,-56.11 Q83.15,-34.44 96.58,-17.22 Z"/>
      <linearGradient id="seal-blue" x1="0" y1="0" x2="1" y2="1">
        <stop offset="0" stop-color="var(--seal-blue-light)"/>
        <stop offset="1" stop-color="var(--seal-blue-dark)"/>
      </linearGradient>
      <linearGradient id="ribbon-blue" x1="0" y1="0" x2="1" y2="0">
        <stop offset="0" stop-color="var(--seal-blue-light)"/>
        <stop offset="1" stop-color="var(--seal-blue-dark)"/>
      </linearGradient>
      <polygon id="star" points="0,-14 4.1,-4.3 14,-4.3 6,1.9 9,12 0,5.8 -9,12 -6,1.9 -14,-4.3 -4.1,-4.3"/>
    </defs>

    <g class="seal" transform="rotate(-4 420 490)">
      <use href="#seal-shape" transform="translate(420 492) scale(3.6 3.5)" fill="url(#seal-blue)"/>
      <use href="#seal-shape" transform="translate(420 492) scale(3.33 3.23)" fill="none" stroke="var(--ink-white)" stroke-width="2" vector-effect="non-scaling-stroke"/>
      <use href="#seal-shape" transform="translate(420 492) scale(3.1 3.0)" fill="var(--seal-red)"/>

      <text class="headline" x="405" y="340" text-anchor="middle" font-size="100" letter-spacing="3">VOTE FOR</text>

      <g class="ribbon">
        <rect x="40" y="370" width="752" height="245" fill="url(#ribbon-blue)"/>
        <line x1="40" y1="397" x2="792" y2="397" stroke="var(--ink-white)" stroke-width="2"/>
        <line x1="40" y1="592" x2="792" y2="592" stroke="var(--ink-white)" stroke-width="2"/>
        <text class="candidate-name" x="412" y="555" text-anchor="middle" font-size="170" textLength="620" lengthAdjust="spacingAndGlyphs">RAMIRO DUVAL</text>
        <g class="ribbon__stars" fill="var(--ink-white)">
          <use href="#star" x="378" y="579"/>
          <use href="#star" x="416" y="577"/>
          <use href="#star" x="454" y="575"/>
        </g>
      </g>

      <text class="office" x="420" y="685" text-anchor="middle" font-size="62" letter-spacing="1">PELLWICK SCHOOL</text>
      <text class="office-seat" x="420" y="720" text-anchor="middle" font-size="34">BOARD PL.</text>
    </g>

    <g class="event-info" transform="rotate(-4 520 950)">
      <text x="522" y="945" text-anchor="middle" font-size="104" letter-spacing="2">DATE:00-00-00</text>
      <text x="528" y="1030" text-anchor="middle" font-size="84" letter-spacing="2">PLACE: XXX</text>
    </g>

    <text class="fine-print" x="425" y="1172" text-anchor="middle">Advertising paid for by candidate</text>
  </svg>
</main>
</body>
</html>
```